Business card for senior move management company
@ Project Holder : Could you extend this contest,please?
Is there latitude with the logo, can we remove the wavy lines if they interfere with the design?
All
there are some excellent design choices already, thank you!
General comments are:
1. The client has asked for her name to be in all capitals with the first letter of each word slightly larger than the rest.
2. The client for this company serves are tyically over 75 years old. The fonts need to be clearly legible, and as large as is practical. The phone number is especially important for size.
3. Vhange from the original spec: the website address should go with the text "Organizing, Downsizing and relocation management"
4. the text "Boston, MA" should go with the phone number and email.
We are still interested in seeing additional creative ideas.
Thanks Again!
Gareth

```html
<!DOCTYPE html>
<html lang="en">
<head>
<meta charset="utf-8">
<title>Gentle Path Moves – Business Card Concepts</title>
<link rel="stylesheet" href="https://fonts.googleapis.com/css2?family=Source+Sans+3:wght@400;700&display=swap">
<style>
  :root {
    --ink: #1d1d1f;
    --card-edge: #3a3a3a;
    --stamp-blue: #2f34d4;
    --band-blue: #0b0be8;
    --band-text: #ffffff;
    --paper: #ffffff;
    --page: #ffffff;
  }
  * { box-sizing: border-box; margin: 0; padding: 0; }
  html, body { width: 1200px; height: 785px; overflow: hidden; background: var(--page); }
  body { position: relative; font-family: "Source Sans 3", Arial, sans-serif; color: var(--ink); }

  .card {
    position: absolute;
    width: 461px;
    height: 263px;
    background: var(--paper);
    border: 2px solid var(--card-edge);
    border-radius: 14px;
    overflow: hidden;
  }
  .card--front-a { left: 132px; top: 113px; }
  .card--back-a  { left: 607px; top: 113px; }
  .card--front-b { left: 132px; top: 401px; }
  .card--back-b  { left: 607px; top: 401px; }

  .brand-mark {
    position: absolute;
    display: flex;
    align-items: center;
    justify-content: center;
    border: 3px solid var(--stamp-blue);
    border-radius: 50%;
    color: var(--stamp-blue);
    font-weight: 700;
    text-align: center;
    line-height: 1.05;
    text-transform: uppercase;
  }
  .brand-mark--small { width: 96px; height: 96px; font-size: 14px; }
  .card--front-a .brand-mark { left: 14px; top: 84px; }
  .card--front-b .brand-mark { left: 14px; top: 74px; }
  .card--back-a .brand-mark { left: 180px; top: 56px; width: 100px; height: 100px; font-size: 15px; }
  .brand-mark--large { left: 142px; top: 42px; width: 176px; height: 176px; font-size: 24px; }

  .divider {
    position: absolute;
    left: 200px;
    width: 2px;
    height: 140px;
    background: var(--stamp-blue);
  }
  .card--front-a .divider { top: 62px; }
  .card--front-b .divider { top: 52px; }

  .contact-block { position: absolute; left: 212px; }
  .card--front-a .contact-block { top: 62px; }
  .card--front-b .contact-block { top: 52px; }
  .contact-name { font-size: 22px; line-height: 30px; letter-spacing: 0.5px; }
  .contact-name .initial { font-size: 29px; }
  .contact-title { font-size: 18px; line-height: 22px; margin-bottom: 12px; }
  .contact-phone { font-size: 19px; line-height: 24px; font-weight: 700; }
  .contact-line { font-size: 15px; line-height: 20px; }

  .band {
    position: absolute;
    left: 0; right: 0; bottom: 0;
    background: var(--band-blue);
  }
  .band--thin { height: 18px; }
  .band--tagline {
    height: 42px;
    display: flex;
    flex-direction: column;
    align-items: center;
    justify-content: center;
    color: var(--band-text);
  }

  .tagline { font-size: 14px; line-height: 17px; text-align: center; }
  .tagline-block { position: absolute; left: 0; right: 0; top: 180px; }
</style>
</head>
<body>

  <section class="card card--front-a" aria-label="Card front, thin band">
    <div class="brand-mark brand-mark--small">Gentle<br>Path<br>Moves</div>
    <div class="divider"></div>
    <div class="contact-block">
      <p class="contact-name"><span class="initial">D</span>ANA <span class="initial">W</span>HITFIELD</p>
      <p class="contact-title">President</p>
      <p class="contact-phone">Phone: (555) 014 2273</p>
      <p class="contact-line">Email: Dana@GPMtransitions.com</p>
      <p class="contact-line">Boston, MA</p>
    </div>
    <div class="band band--thin"></div>
  </section>

  <section class="card card--back-a" aria-label="Card back with tagline">
    <div class="brand-mark brand-mark--small">Gentle<br>Path<br>Moves</div>
    <div class="tagline-block">
      <p class="tagline">"Organizing, Downsizing &amp; Relocation Management"</p>
      <p class="tagline">www.GPMtransitions.com</p>
    </div>
  </section>

  <section class="card card--front-b" aria-label="Card front, tagline band">
    <div class="brand-mark brand-mark--small">Gentle<br>Path<br>Moves</div>
    <div class="divider"></div>
    <div class="contact-block">
      <p class="contact-name"><span class="initial">D</span>ANA <span class="initial">W</span>HITFIELD</p>
      <p class="contact-title">President</p>
      <p class="contact-phone">Phone: (555) 014 2273</p>
      <p class="contact-line">Email: Dana@GPMtransitions.com</p>
      <p class="contact-line">Boston, MA</p>
    </div>
    <div class="band band--tagline">
      <p class="tagline">"Organizing, Downsizing &amp; Relocation Management"</p>
      <p class="tagline">www.GPMtransitions.com</p>
    </div>
  </section>

  <section class="card card--back-b" aria-label="Card back with large brand mark">
    <div class="brand-mark brand-mark--large">Gentle<br>Path<br>Moves</div>
  </section>

</body>
</html>
```